Letter head for peronal trainer

Letter head top and bottom. Elite looking design that looks modern and prestigious for high end clients. Black, silver, reds etc. Attached are my business cards (2 x pdfs) and my website is: www.dariomokhtar.net for style/ideas

Needs to look good when printing and be locked onto the page when people use my word docs on the computer, I don't want it to be 'clickable' if you know what I mean. Needs to work in A4 in portrait (and in landscape, for programme cards). I need it to be editable for when I adjust the text myself. Needs my contact details and social media details and title personal trainer (Central London/Greenwich/Blackheath) and Online Distance Coaching. . A little picture at the bottom too if it works (Like the vest one)

```html
<!DOCTYPE html>
<html lang="en">
<head>
<meta charset="utf-8">
<title>Dario Mokhtar – Personal Trainer Letterhead</title>
<link rel="stylesheet" href="https://fonts.googleapis.com/css2?family=Archivo:ital,wght@0,400;0,500;1,400;1,900&display=swap">
<style>
  :root {
    --backdrop: #e6e6e6;
    --paper: #ffffff;
    --header-black: #050505;
    --silver-light: #ffffff;
    --silver-dark: #a9a9ab;
    --header-text: #f2f2f2;
    --ink: #111111;
    --navy: #1f2a6b;
    --photo-dark: #2a2a2a;
    --photo-mid: #6b6b6b;
    --photo-fade: #c9ccd2;
  }
  * { box-sizing: border-box; margin: 0; padding: 0; }
  html, body {
    width: 1091px; height: 1200px; overflow: hidden;
    background: var(--backdrop);
    font-family: "Archivo", Arial, sans-serif;
  }
  .letterhead {
    position: absolute; left: 177px; top: 79px;
    width: 736px; height: 1042px;
    background: var(--paper);
    box-shadow: 0 2px 10px rgba(0,0,0,0.18);
    overflow: hidden;
  }
  .masthead {
    position: absolute; left: 0; top: 0; width: 100%; height: 177px;
    background: var(--header-black);
  }
  .masthead__portrait {
    position: absolute; left: 570px; top: 0; width: 136px; height: 177px;
    background: radial-gradient(ellipse at 55% 55%, var(--photo-mid) 0%, var(--photo-dark) 45%, var(--header-black) 80%);
  }
  .masthead__name, .masthead__title, .masthead__areas {
    position: absolute; z-index: 1; white-space: nowrap;
  }
  .masthead__name {
    left: 26px; top: 22px;
    font-size: 50px; font-weight: 900; font-style: italic;
    letter-spacing: 1px; line-height: 1;
    background: linear-gradient(180deg, var(--silver-light) 20%, var(--silver-dark) 90%);
    -webkit-background-clip: text; background-clip: text; color: transparent;
  }
  .masthead__title {
    left: 27px; top: 88px;
    font-size: 36px; font-weight: 400; font-style: italic;
    letter-spacing: 3px; line-height: 1; color: var(--header-text);
  }
  .masthead__areas {
    left: 27px; top: 140px;
    font-size: 16px; font-weight: 500; letter-spacing: 1.8px;
    line-height: 1; color: var(--header-text);
  }
  .footer-photo {
    position: absolute; left: 429px; top: 611px; width: 307px; height: 431px;
    background:
      linear-gradient(90deg, var(--paper) 0%, rgba(255,255,255,0) 35%),
      linear-gradient(180deg, var(--paper) 0%, rgba(255,255,255,0) 30%),
      radial-gradient(ellipse at 60% 55%, #a9adb6 0%, var(--photo-fade) 45%, #eef0f3 80%);
  }
  .tagline {
    position: absolute; left: 14px; top: 922px; white-space: nowrap;
    font-size: 22px; font-weight: 500; letter-spacing: 1.5px;
    line-height: 1; color: var(--ink);
  }
  .tagline-rule {
    position: absolute; left: 0; top: 954px; width: 470px; height: 4px;
    background: linear-gradient(90deg, var(--navy) 0%, var(--navy) 55%, rgba(31,42,107,0) 100%);
  }
  .contacts {
    position: absolute; left: 0; top: 978px; width: 520px; height: 50px;
    font-size: 15px; color: var(--navy); letter-spacing: 0.5px;
  }
  .contact {
    position: absolute; display: flex; align-items: center; gap: 12px;
    line-height: 1; white-space: nowrap;
  }
  .contact svg { width: 14px; height: 14px; fill: var(--navy); flex: none; }
  .contact--phone { left: 18px; top: 2px; }
  .contact--email { left: 18px; top: 26px; }
  .contact--web { left: 276px; top: 2px; }
  .contact--social { left: 276px; top: 26px; }
</style>
</head>
<body>
  <main class="letterhead">
    <header class="masthead">
      <div class="masthead__portrait" role="img" aria-label="Dark studio photograph of the trainer's muscular torso"></div>
      <h1 class="masthead__name">DARIO MOKHTAR</h1>
      <p class="masthead__title">PERSONAL TRAINER</p>
      <p class="masthead__areas">CENTRAL LONDON/GREENWICH/BLACKHEATH</p>
    </header>

    <div class="footer-photo" role="img" aria-label="Faded photograph of the trainer in a vest lifting dumbbells"></div>

    <p class="tagline">ONLINE DISTANCE COACHING</p>
    <div class="tagline-rule"></div>

    <footer class="contacts">
      <div class="contact contact--phone">
        <svg viewBox="0 0 16 16" aria-hidden="true"><path d="M3.5 1.5l2.5 0 1 3.5-1.7 1.2c.8 1.8 2.2 3.2 4 4l1.2-1.7 3.5 1v2.5c0 .8-.7 1.5-1.5 1.5C6.7 13.5 2 8.8 2 3c0-.8.7-1.5 1.5-1.5z"/></svg>
        <span>0770090123</span>
      </div>
      <div class="contact contact--email">
        <svg viewBox="0 0 16 16" aria-hidden="true"><circle cx="8" cy="8" r="7" fill="none" stroke="#1f2a6b" stroke-width="1.6"/><path d="M1 8h14M8 1c2.2 2 2.2 12 0 14M8 1c-2.2 2-2.2 12 0 14" fill="none" stroke="#1f2a6b" stroke-width="1.3"/></svg>
        <span>dario.mPT@mailpost.net</span>
      </div>
      <div class="contact contact--web">
        <svg viewBox="0 0 16 16" aria-hidden="true"><path d="M1 3h14v10H1z"/><path d="M1.5 3.5L8 9l6.5-5.5" fill="none" stroke="#ffffff" stroke-width="1.4"/></svg>
        <span>www.dariomokhtar.net</span>
      </div>
      <div class="contact contact--social">
        <svg viewBox="0 0 16 16" aria-hidden="true"><circle cx="8" cy="8" r="6.5"/></svg>
        <span>@dariomk_2</span>
      </div>
    </footer>
  </main>
</body>
</html>
```